Buch-/E-Book-Cover für Ratgeber gesucht
Zielgruppe
Es handelt sich um einen Ratgeber zum Thema 'Das Tor zur Heiterkeit: Wie du es endlich lernst, gelassen zu leben!'.
Das Buch richtet sich vor allem an Frauen im Alter zwischen 18-45 Jahren.
Wie der Titel des Buches bereits aussagt, besteht das Buch aus verschiedenen Kapiteln zum Thema: 'Wie man glücklich wird'.
Aufgabenstellung
*UPDATE: 16.02.2023 / 19:00 Uhr*
Ich habe Beispielcover (1-7) hochgeladen, die ihr als Inspiration für eure Covervorschläge nutzen könnt. Es sollten natürlich keine 1:1 Kopien sein.
Danke!
1.) Der Haupttitel des Buches lautet 'Das Tor zur Heiterkeit'
2.) Der Untertitel des Buches lautet 'Wie du es endlich lernst, gelassen zu leben!'
3.) Der Name der Autorin lautet 'Lore Brandt'
4.) Der Verlagsname lautet 'deine Morgenruhe'.
5.)Das Cover sollte eine Mischung aus 'modern/schlicht' und 'klassisch' sein und nach Möglichkeit Elemente enthalten wie:
- der Hintergrund aus einer Pastellfarbe. Wichtige Elemente können jedoch mit einer Kontrastfarbe hervorgehoben werden
- kein 'eintöniger/einfarbiger' Hintergrund, sondern z. B. mit einem 'Muster'
- Der Haupttitel kann gerne aus verschiedenen Schriftarten bestehen (modern/klassisch) und etwas größer sein, damit er direkt ersichtlich ist.
- aussagekräftige(s) Symbol(e) passend zum Titel ('Das Tor zur Heiterkeit').
- Vektorgrafiken/-elemente anstelle von 'Fotos'
6.) Es wird ein Cover für ein Ebook, Taschenbuch als auch Hardcover benötigt.
7.) Das Buch hat ca. 229 Seiten und ein Format von 6x9 Zoll. Die Formatvorlage für Bookora und andere Plattformen kann gerne zu Verfügung gestellt werden.
8.) Ich besitze eine kostenpflichtige Lizenz bei grafomint, sodass hier gerne jede Grafik bezogen werden kann. Wenn eine Grafik nur auf einer anderen Plattform vorhanden ist, dann bin ich bereit diese zu kaufen.
9.) Es werden weitere Bücher in dem Themengebiet folgen, sodass eine langfristige Kooperation zum Designen von Covern angedacht ist.

```html
<!DOCTYPE html>
<html lang="de">
<head>
<meta charset="utf-8">
<title>Das Tor zur Heiterkeit – Lore Brandt</title>
<link rel="stylesheet" href="https://fonts.googleapis.com/css2?family=Montserrat:wght@600;700&family=Kaushan+Script&family=Cinzel:wght@500&family=Libre+Baskerville&display=swap">
<style>
  :root {
    --page-bg: #f2f2f0;
    --sky-top: #b4e0e0;
    --sky-mid: #d8f0f2;
    --sky-light: #e9f6f7;
    --blossom: #e8bca8;
    --meadow: #6cc0b0;
    --meadow-deep: #3e9a88;
    --figure-light: #f0cfc4;
    --figure-dark: #22405c;
    --author: #1d6478;
    --teal: #1ba19e;
    --coral: #ef5c5a;
    --gold-light: #f4dc8e;
    --gold: #d9ad4c;
    --gold-dark: #b3872c;
    --navy: #1e4d6b;
    --white: #ffffff;
  }
  html, body {
    margin: 0;
    width: 1166px;
    height: 1200px;
    overflow: hidden;
    background: var(--page-bg);
  }
  .cover {
    position: absolute;
    left: 188px;
    top: 0;
    width: 790px;
    height: 1200px;
    overflow: hidden;
    background: linear-gradient(180deg, var(--sky-top) 0%, var(--sky-mid) 40%, var(--sky-light) 58%, var(--sky-mid) 100%);
  }
  .photo-meadow {
    position: absolute;
    left: 0; right: 0; bottom: 0;
    height: 460px;
    background: linear-gradient(180deg,
      rgba(232,188,168,0) 0%,
      rgba(232,188,168,.45) 30%,
      rgba(108,192,176,.75) 65%,
      var(--meadow-deep) 100%);
  }
  .photo-figure {
    position: absolute;
    left: 560px; top: 700px;
    width: 190px; height: 500px;
    border-radius: 95px 95px 0 0;
    background: linear-gradient(180deg, var(--figure-light) 0%, #b48a86 28%, var(--figure-dark) 48%, var(--figure-dark) 100%);
    opacity: .85;
  }
  .author {
    position: absolute;
    top: 108px; left: 0; right: 0;
    margin: 0;
    text-align: center;
    font-family: "Montserrat", sans-serif;
    font-weight: 600;
    font-size: 32px;
    letter-spacing: 3px;
    color: var(--author);
  }
  .title { margin: 0; font-weight: normal; }
  .title span {
    position: absolute;
    left: 0; right: 0;
    display: block;
    text-align: center;
    line-height: 1;
  }
  .title .caps {
    font-family: "Cinzel", serif;
    font-weight: 500;
    font-size: 64px;
    letter-spacing: 14px;
    color: var(--teal);
  }
  .title .script {
    font-family: "Kaushan Script", cursive;
    color: var(--coral);
    transform: rotate(-4deg);
  }
  .caps-1 { top: 212px; }
  .script-1 { top: 262px; font-size: 200px; }
  .caps-2 { top: 448px; }
  .script-2 { top: 500px; font-size: 150px; }
  .subtitle {
    position: absolute;
    top: 700px; left: 0; right: 0;
    margin: 0;
    text-align: center;
    font-family: "Libre Baskerville", serif;
    font-size: 29px;
    line-height: 43px;
    color: var(--teal);
  }
  .badge {
    position: absolute;
    left: 56px; top: 848px;
    width: 200px; height: 200px;
  }
  .badge svg { position: absolute; inset: 0; }
  .badge-text {
    position: absolute;
    inset: 0;
    display: flex;
    flex-direction: column;
    align-items: center;
    justify-content: center;
    transform: rotate(-8deg);
    font-family: "Montserrat", sans-serif;
    font-weight: 700;
    font-size: 19px;
    line-height: 21px;
    color: var(--white);
    text-align: center;
  }
  .badge-number {
    font-family: "Libre Baskerville", serif;
    font-weight: 400;
    font-size: 50px;
    line-height: 50px;
    color: var(--navy);
  }
  .publisher {
    position: absolute;
    top: 1112px; left: 0; width: 560px;
    margin: 0;
    text-align: center;
    font-family: "Libre Baskerville", serif;
    font-size: 26px;
    color: var(--white);
  }
</style>
</head>
<body>
  <main class="cover">
    <div class="photo-meadow" role="img" aria-label="Foto: Blumenwiese mit zarten rosa Blüten vor hellem Himmel"></div>
    <div class="photo-figure" role="img" aria-label="Foto: junge Frau im dunkelblauen Shirt mit einer roten Mohnblume, im Gegenlicht"></div>

    <p class="author">LORE BRANDT</p>

    <h1 class="title">
      <span class="caps caps-1">DAS</span>
      <span class="script script-1">Tor</span>
      <span class="caps caps-2">ZUR</span>
      <span class="script script-2">Heiterkeit</span>
    </h1>

    <p class="subtitle">Wie du es<br>endlich lernst,<br>gelassen zu leben!</p>

    <div class="badge">
      <svg width="200" height="200" viewBox="-103 -103 206 206" aria-hidden="true">
        <defs>
          <linearGradient id="gold-fill" x1="0" y1="0" x2="1" y2="1">
            <stop offset="0" stop-color="var(--gold-light)"/>
            <stop offset=".5" stop-color="var(--gold)"/>
            <stop offset="1" stop-color="var(--gold-dark)"/>
          </linearGradient>
        </defs>
        <polygon fill="url(#gold-fill)" points="0,-100 17,-88 38,-92 48,-73 69,-69 72,-47 89,-34 82,-14 95,3 82,20 86,41 66,51 58,72 37,73 21,90 0,82 -21,90 -37,73 -58,72 -66,51 -86,41 -82,20 -95,3 -82,-14 -89,-34 -72,-47 -69,-69 -48,-73 -38,-92 -17,-88"/>
      </svg>
      <div class="badge-text">
        <span>Mit</span>
        <span class="badge-number">66</span>
        <span>inspirierenden</span>
        <span>Gedanken</span>
        <span>&amp; Tipps</span>
      </div>
    </div>

    <p class="publisher">deineMorgenruhe.de</p>
  </main>
</body>
</html>
```